Business Card Design Project

We need a new business card design that will allow us to incorporate three different logos. All three logos fall under our corporate name, Voltaro, Inc. Our current business card only has one logo on it. We have logo for our mobile printer division, a logo for our dot-matrix division, and a logo for our custom solutions division. I'd like all three logos to be on the new business card. I'd like the business card to have the same color scheme as our corporate web site: www.voltaro-example.com. We are a technology company that manufactures dot-matrix and mobile thermal printer. We also do custom OEM products as well.

Industry/Entity Type

Printer

Requirements
Must have
• all three logos on the business card

```html
<!DOCTYPE html>
<html lang="en">
<head>
<meta charset="utf-8">
<title>Voltaro, Inc. – Business Card</title>
<link rel="stylesheet" href="https://fonts.googleapis.com/css2?family=Open+Sans:wght@400;600;700&display=swap">
<style>
  :root {
    --sky-deep: #1f63b0;
    --sky-mid: #5d9bd8;
    --sky-light: #bcd8f0;
    --paper: #ffffff;
    --ink: #111111;
    --brand-navy: #16284a;
    --brand-blue: #1f63b0;
    --trim: #333333;
  }
  * { margin: 0; padding: 0; box-sizing: border-box; }
  html, body {
    width: 1200px;
    height: 900px;
    overflow: hidden;
    background: var(--paper);
    font-family: "Open Sans", Arial, sans-serif;
    color: var(--ink);
  }
  .canvas { position: relative; width: 1200px; height: 900px; }

  .trim-marks { position: absolute; inset: 0; }

  .card {
    position: absolute;
    left: 64px;
    top: 90px;
    width: 1072px;
    height: 678px;
    background: var(--paper);
    overflow: hidden;
  }
  .card__sky {
    position: absolute;
    left: 0; top: 0;
    width: 100%;
    height: 480px;
    background:
      radial-gradient(ellipse 260px 90px at 560px 210px, rgba(255,255,255,0.35), rgba(255,255,255,0) 70%),
      radial-gradient(ellipse 180px 60px at 760px 100px, rgba(255,255,255,0.3), rgba(255,255,255,0) 70%),
      radial-gradient(ellipse 160px 55px at 180px 150px, rgba(255,255,255,0.25), rgba(255,255,255,0) 70%),
      radial-gradient(ellipse 220px 80px at 900px 260px, rgba(255,255,255,0.3), rgba(255,255,255,0) 70%),
      linear-gradient(to bottom, var(--sky-deep) 0%, var(--sky-mid) 35%, var(--sky-light) 65%, var(--paper) 100%);
  }

  .contact {
    position: absolute;
    right: 92px;
    top: 88px;
    text-align: right;
  }
  .contact__name {
    font-size: 36px;
    font-weight: 600;
    line-height: 44px;
  }
  .contact__title {
    font-size: 26px;
    font-weight: 400;
    line-height: 32px;
  }
  .contact__address {
    margin-top: 56px;
    font-style: normal;
    font-size: 24px;
    line-height: 30px;
  }
  .contact__web {
    margin-top: 32px;
    font-size: 27px;
    font-weight: 600;
    line-height: 36px;
  }

  .divisions {
    position: absolute;
    left: 72px;
    right: 92px;
    top: 568px;
    display: flex;
    align-items: center;
    justify-content: space-between;
  }
  .division {
    display: flex;
    align-items: center;
    gap: 12px;
    color: var(--brand-navy);
    font-size: 26px;
    font-weight: 700;
    white-space: nowrap;
  }
  .division__mark {
    flex: none;
    width: 30px;
    height: 30px;
    background: var(--brand-blue);
  }
  .division__mark--round { border-radius: 50%; width: 44px; height: 44px; }
</style>
</head>
<body>
<main class="canvas">
  <svg class="trim-marks" width="1200" height="900" viewBox="0 0 1200 900" aria-hidden="true">
    <g stroke="var(--trim)" stroke-width="2">
      <line x1="100" y1="60" x2="100" y2="82"/>
      <line x1="1100" y1="60" x2="1100" y2="82"/>
      <line x1="64" y1="770" x2="90" y2="770"/>
      <line x1="100" y1="776" x2="100" y2="800"/>
      <line x1="1110" y1="770" x2="1136" y2="770"/>
      <line x1="1100" y1="776" x2="1100" y2="800"/>
    </g>
  </svg>

  <section class="card">
    <div class="card__sky" role="img" aria-label="Soft blue sky backdrop with translucent floating light bubbles"></div>

    <div class="contact">
      <h1 class="contact__name">Marten Halvorsen</h1>
      <p class="contact__title">Head of Print Development</p>
      <address class="contact__address">
        Voltaro, Inc.<br>
        2840 Orchard Ridge Road<br>
        Lakeview Falls, MI 49100<br>
        Toll Free: 800.555.0147<br>
        Telephone: 269.555.0182<br>
        Fax: 269.555.0190
      </address>
      <p class="contact__web">
        m.halvorsen@voltaro-example.com<br>
        www.voltaro-example.com
      </p>
    </div>

    <div class="divisions">
      <div class="division division--mobile">
        <span class="division__mark"></span>
        <span class="division__name">Voltaro Mobile</span>
      </div>
      <div class="division division--dot-matrix">
        <span class="division__name">Voltaro</span>
      </div>
      <div class="division division--custom">
        <span class="division__mark division__mark--round"></span>
        <span class="division__name">Voltaro Custom Solutions</span>
      </div>
    </div>
  </section>
</main>
</body>
</html>
```